依頼詳細
当院がこの度4月より、木曜診療・駐車場提携・CT導入をしたため、そのお知らせのチラシを作成いただきたいです。(A4裏表)
ラフ・素材等はございます。HP(http://mk-dental.net/)取っていただいても構いません。

※発送はポミネオ様で行う予定です。(https://pomineo.com/directmail/large-sized-postcard/
※まず表面案だけで構いませんのでお出しいただけますと幸いです。その後当選の方が決まり次第裏面もお願いしようと思います。
記載項目
添付ラフ通り
サイズ
A4
ページ数
両面
希望イメージ
シンプル 複雑
単色 カラフル
暗い 明るい
日常 高級
遊び心 厳粛
未来的 伝統的
女性的 男性的
希望する色
緑系
納品ファイル
• イラストレーター形式 (.ai)
• PNG形式 (.png)
補足説明
ポミネオのDM(https://pomineo.com/directmail/large-sized-postcard/)で患者様に発送するため、ポミネオの規定で作成願えますでしょうか。
■ 選んだ理由

全体的なデザインバランスが良かったため

■ 提案者全員のお礼・コメント

この度はご参加いただきまして誠に有難うございました!
今後とも宜しくお願いいたします。

```html
<!DOCTYPE html>
<html lang="ja">
<head>
<meta charset="utf-8">
<title>松川ファミリー歯科からのご案内</title>
<link href="https://fonts.googleapis.com/css2?family=M+PLUS+Rounded+1c:wght@400;700;800&family=Noto+Sans+JP:wght@400;700;900&display=swap" rel="stylesheet">
<style>
:root{
  --green:#4caf3e;
  --green-dark:#2f8a2a;
  --green-light:#dff0d6;
  --green-pale:#eef7e8;
  --pink:#e8467c;
  --pink-light:#fbe1ea;
  --yellow:#f4d33a;
  --ink:#333;
  --grey:#777;
  --white:#fff;
}
*{box-sizing:border-box;margin:0;padding:0}
html,body{width:851px;height:1200px;overflow:hidden}
body{background:var(--green-pale);font-family:"Noto Sans JP",sans-serif;color:var(--ink);position:relative}
.header{position:absolute;left:0;top:0;width:851px;height:88px;background:var(--white);border-bottom:6px solid var(--green);display:flex;align-items:center;padding-left:40px;gap:14px}
.brand{display:flex;align-items:center;gap:10px}
.brand-dot{width:40px;height:40px;border-radius:50%;background:var(--green)}
.brand-name{font-family:"M PLUS Rounded 1c",sans-serif;font-weight:800;font-size:34px;color:var(--green-dark);line-height:1}
.brand-sub{font-family:"M PLUS Rounded 1c",sans-serif;font-weight:800;font-size:10px;color:var(--green-dark);letter-spacing:1px;margin-top:4px}
.header-tail{font-family:"M PLUS Rounded 1c",sans-serif;font-weight:800;font-size:34px;color:var(--green-dark);margin-left:8px}
.card{position:absolute;background:var(--white);border-radius:14px;box-shadow:0 2px 0 rgba(0,0,0,.08);overflow:hidden}
.hours{left:22px;top:102px;width:807px;height:300px}
.hours-title{position:absolute;left:18px;top:14px;width:770px;height:84px;background:var(--green-light);border-radius:10px;border-left:14px solid var(--green);padding:6px 24px;font-family:"M PLUS Rounded 1c",sans-serif;font-weight:800}
.hours-title .line1{font-size:26px;color:var(--ink);line-height:1.2}
.hours-title .line2{font-size:36px;color:var(--ink);line-height:1.2}
.hours-title .line2 em{font-style:normal;color:var(--green-dark)}
.old-table{position:absolute;left:36px;top:114px;width:160px;font-size:9px;color:var(--grey)}
.old-table table,.new-table table{border-collapse:collapse;width:100%}
.old-table td,.old-table th{border-bottom:1px solid #ccc;text-align:center;padding:3px 0;font-weight:400}
.staff-art{position:absolute;left:30px;top:184px;width:140px;height:90px;border-radius:8px;background:linear-gradient(#f7efe4,#efe2d2)}
.bubble{position:absolute;left:186px;top:222px;width:96px;height:50px;border:2px solid var(--green);border-radius:50%;font-size:10px;text-align:center;padding-top:10px;line-height:1.3;background:var(--white)}
.new-table{position:absolute;left:300px;top:112px;width:490px}
.new-table table{table-layout:fixed}
.new-head{display:inline-block;background:var(--pink-light);border-radius:14px;padding:3px 16px;font-weight:700;font-size:15px;color:var(--pink);margin-bottom:6px}
.new-head::before{content:"●";margin-right:4px}
.new-table th{font-size:17px;font-weight:900;padding:2px 0;border-bottom:2px solid var(--green)}
.new-table th:first-child,.new-table td.time{width:104px}
.new-table td{text-align:center;padding:5px 0;border-bottom:1px solid #ccc;font-size:16px;height:44px}
.new-table td.time{font-size:13px;font-weight:700;line-height:1.15}
.new-table .thu{background:var(--pink-light)}
.dot{display:inline-block;width:14px;height:14px;border-radius:50%;background:var(--ink);vertical-align:middle}
.thu .dot{background:var(--pink)}
.closed{text-align:right;font-size:14px;font-weight:700;color:var(--pink);margin-top:6px}
.closed span{color:var(--ink)}
.parking{left:22px;top:414px;width:490px;height:642px}
.section-title{font-family:"M PLUS Rounded 1c",sans-serif;font-weight:800;font-size:30px}
.parking .section-title{position:absolute;left:20px;top:14px;color:var(--pink);border-bottom:4px dotted var(--pink);padding-bottom:4px}
.map{position:absolute;left:20px;top:70px;width:450px;height:470px;border-radius:6px;background:linear-gradient(135deg,#f6f6f1,#e9ede2)}
.map-bubble{position:absolute;left:250px;top:88px;width:150px;height:66px;border:2px solid var(--pink);border-radius:50%;background:var(--white);font-size:13px;text-align:center;padding-top:14px;line-height:1.35}
.lot{position:absolute;background:var(--pink);color:var(--white);font-size:12px;font-weight:700;padding:3px 8px;border-radius:3px}
.free{position:absolute;left:20px;top:554px;width:200px;height:40px;background:var(--pink);color:var(--white);font-weight:900;font-size:20px;display:flex;align-items:center;justify-content:center;border-radius:4px}
.note{position:absolute;right:20px;top:610px;font-size:10px;color:var(--grey)}
.ct{left:524px;top:414px;width:305px;height:642px}
.ct .section-title{position:absolute;left:16px;top:16px;font-size:22px;color:var(--white);background:var(--green);padding:8px 14px;border-radius:8px;line-height:1.3}
.ct-body{position:absolute;left:18px;top:120px;width:270px}
.ct-body h3{font-size:15px;color:var(--green-dark);margin-bottom:8px}
.ct-body li{list-style:none;font-size:10.5px;line-height:1.5;margin-bottom:10px;padding-left:24px;position:relative}
.ct-body li::before{content:"";position:absolute;left:0;top:3px;width:14px;height:14px;background:var(--yellow);border-radius:3px}
.ct-art{position:absolute;left:18px;top:420px;width:270px;height:200px;border-radius:6px;background:linear-gradient(#f4f4f4,#dcdcdc)}
.footer{position:absolute;left:0;top:1070px;width:851px;height:130px;background:var(--white);padding:18px 40px}
.phone{display:flex;align-items:center;gap:8px;font-family:"M PLUS Rounded 1c",sans-serif;font-weight:800;font-size:48px;color:var(--green-dark);line-height:1}
.address{font-size:13px;margin-top:14px}
.footer .brand{position:absolute;right:40px;top:30px}
.footer .brand-name{font-size:30px}
</style>
</head>
<body>
<header class="header">
  <div class="brand">
    <div class="brand-dot"></div>
    <div><div class="brand-name">松川ファミリー歯科</div><div class="brand-sub">MATSUKAWA FAMILY DENTAL CLINIC</div></div>
  </div>
  <div class="header-tail">からのご案内</div>
</header>

<section class="card hours">
  <div class="hours-title"><div class="line1">4月1日より</div><div class="line2"><em>木曜日の診療を開始</em>します</div></div>
  <div class="old-table">
    <div>＜これまでの診療時間＞</div>
    <table>
      <tr><th></th><th>月</th><th>火</th><th>水</th><th>木</th><th>金</th><th>土</th></tr>
      <tr><td>10:00-</td><td>●</td><td>●</td><td>●</td><td>×</td><td>●</td><td>●</td></tr>
      <tr><td>14:30-</td><td>●</td><td>●</td><td>●</td><td>×</td><td>●</td><td>●</td></tr>
    </table>
  </div>
  <div class="staff-art" role="img" aria-label="医師と歯科衛生士のイラスト"></div>
  <div class="bubble">ご利用しやすく<br>なります！</div>
  <div class="new-table">
    <div class="new-head">4月1日からの診療時間</div>
    <table>
      <tr><th></th><th>月</th><th>火</th><th>水</th><th class="thu">木</th><th>金</th><th>土</th></tr>
      <tr><td class="time">10:00<br>〜13:00</td><td><i class="dot"></i></td><td><i class="dot"></i></td><td><i class="dot"></i></td><td class="thu"><i class="dot"></i></td><td><i class="dot"></i></td><td><i class="dot"></i></td></tr>
      <tr><td class="time">14:30<br>〜20:00</td><td><i class="dot"></i></td><td><i class="dot"></i></td><td><i class="dot"></i></td><td class="thu"><i class="dot"></i></td><td><i class="dot"></i></td><td><i class="dot"></i></td></tr>
    </table>
    <div class="closed">休診日：<span>日曜日・祝日</span></div>
  </div>
</section>

<section class="card parking">
  <h2 class="section-title">駐車場サービスのご案内</h2>
  <div class="map" role="img" aria-label="医院周辺と提携駐車場の位置を示す地図"></div>
  <span class="lot" style="left:40px;top:148px">パークス松川2丁目第4</span>
  <span class="lot" style="left:40px;top:198px">パークス松川2丁目第2</span>
  <span class="lot" style="left:200px;top:248px">パークス松川2丁目第3</span>
  <span class="lot" style="left:40px;top:328px">パークス松川2丁目第1</span>
  <span class="lot" style="left:270px;top:398px">パークス松川東第2</span>
  <span class="lot" style="left:40px;top:468px">パークス松川東第1</span>
  <div class="map-bubble">ご来院が、<br>より簡単に！</div>
  <div class="free">40分〜60分無料</div>
  <div class="note">※駐車券は受付でお渡しします</div>
</section>

<section class="card ct">
  <h2 class="section-title">歯科用CTを<br>導入しました</h2>
  <div class="ct-body">
    <h3>CTでできること</h3>
    <ul>
      <li>歯や骨の状態を立体的に確認でき、より正確な診断が可能になります。</li>
      <li>親知らずや神経の位置を事前に把握し、安全な抜歯や治療につなげます。</li>
      <li>インプラント治療の計画を精密に立てることができます。</li>
      <li>撮影時間は短く、被ばく量も少ないため安心して受けていただけます。</li>
    </ul>
  </div>
  <div class="ct-art" role="img" aria-label="歯科用CT装置の写真"></div>
</section>

<footer class="footer">
  <div class="phone">
    <svg width="40" height="40" viewBox="0 0 24 24" aria-hidden="true"><path fill="#2f8a2a" d="M6.6 10.8a15.1 15.1 0 0 0 6.6 6.6l2.2-2.2a1 1 0 0 1 1-.25 11.4 11.4 0 0 0 3.6.57 1 1 0 0 1 1 1V20a1 1 0 0 1-1 1A17 17 0 0 1 3 4a1 1 0 0 1 1-1h3.5a1 1 0 0 1 1 1c0 1.25.2 2.45.57 3.57a1 1 0 0 1-.25 1z"/></svg>
    06-6000-4812
  </div>
  <div class="address">〒500-0000 大阪府みどり市松川区本町2丁目1-8</div>
  <div class="brand">
    <div class="brand-dot"></div>
    <div><div class="brand-name">松川ファミリー歯科</div><div class="brand-sub">MATSUKAWA FAMILY DENTAL CLINIC</div></div>
  </div>
</footer>
</body>
</html>
```